Velvet Orchid Beauty Bar Business Card

We need a modern, elegant business card design for our new beauty bar located in La Quinta, CA. The card should feel premium yet approachable, reflecting our brand identity: warm, stylish, and confidence-boosting.

Use our existing Velvet Orchid Beauty Bar logo (to be provided as vector file).

Colors: Black, White, Blush / Nude accents, and Gold (metallic or foil effect if possible).

Typography: Clean sans-serif for clarity, with optional elegant script accent.
Design Style

Minimalist and modern with plenty of white space.

Premium look with a beauty/lifestyle feel (not overly corporate).

Option to explore vertical or horizontal orientation.

Rounded corners welcome, but not required.

Additional Notes

Design should print well in both matte and glossy finishes.

Please present mockups with both light and dark backgrounds.

Keep overall feel sleek, feminine, and high-end while still being approachable.

```html
<!DOCTYPE html>
<html lang="en">
<head>
<meta charset="utf-8">
<title>Velvet Orchid Beauty Bar – Business Card</title>
<link rel="stylesheet" href="https://fonts.googleapis.com/css2?family=Montserrat:wght@400;500;700&display=swap">
<style>
  :root {
    --stage: #2b2b2b;
    --card-dark: #151515;
    --card-light: #ffffff;
    --ink: #111111;
    --ink-soft: #333333;
    --paper-text: #f2f2f2;
  }
  html, body {
    margin: 0;
    padding: 0;
    overflow: hidden;
  }
  body {
    width: 1200px;
    height: 875px;
    background: var(--stage);
    font-family: "Montserrat", sans-serif;
    display: flex;
    align-items: center;
    justify-content: center;
    gap: 40px;
  }
  .card {
    width: 540px;
    height: 310px;
    border-radius: 22px;
    box-sizing: border-box;
    position: relative;
  }
  .card--front {
    background: var(--card-dark);
    display: flex;
    align-items: center;
    justify-content: center;
  }
  .card--back {
    background: var(--card-light);
    display: flex;
    align-items: center;
    padding: 0 36px 0 30px;
  }
  .brand-name {
    font-weight: 500;
    text-align: center;
    letter-spacing: 0.04em;
    line-height: 1.2;
  }
  .card--front .brand-name {
    color: var(--paper-text);
    font-size: 34px;
  }
  .card--back .brand-name {
    color: var(--ink);
    font-size: 19px;
    width: 215px;
  }
  .divider {
    width: 2px;
    height: 150px;
    background: var(--ink);
    margin: 0 22px;
  }
  .contact {
    color: var(--ink);
    font-size: 13px;
    line-height: 1.35;
  }
  .contact__name {
    font-weight: 700;
    font-size: 22px;
    margin: 0;
  }
  .contact__title {
    font-size: 12px;
    color: var(--ink-soft);
    margin: 0 0 14px;
  }
  .contact__address {
    margin: 0 0 14px;
    color: var(--ink-soft);
  }
  .contact__list {
    list-style: none;
    margin: 0;
    padding: 0;
  }
  .contact__list li {
    display: flex;
    align-items: center;
    gap: 8px;
    margin-bottom: 3px;
  }
  .contact__list svg {
    width: 12px;
    height: 12px;
    fill: var(--ink);
    flex: none;
  }
</style>
</head>
<body>
  <section class="card card--front">
    <div class="brand-name">Velvet Orchid<br>Beauty Bar</div>
  </section>

  <section class="card card--back">
    <div class="brand-name">Velvet Orchid<br>Beauty Bar</div>
    <div class="divider"></div>
    <div class="contact">
      <p class="contact__name">Elena Ward</p>
      <p class="contact__title">Managing Director</p>
      <p class="contact__address">48 Palm Court,<br>Riverton, USA</p>
      <ul class="contact__list">
        <li>
          <svg viewBox="0 0 24 24" aria-hidden="true"><path d="M6.6 10.8a15.5 15.5 0 0 0 6.6 6.6l2.2-2.2a1 1 0 0 1 1-.25 11.4 11.4 0 0 0 3.6.57 1 1 0 0 1 1 1V20a1 1 0 0 1-1 1A17 17 0 0 1 3 4a1 1 0 0 1 1-1h3.5a1 1 0 0 1 1 1c0 1.25.2 2.45.57 3.6a1 1 0 0 1-.25 1z"/></svg>
          (08) 4410 2276
        </li>
        <li>
          <svg viewBox="0 0 24 24" aria-hidden="true"><path d="M2 5h20v14H2z M2 5l10 8 10-8" fill="none" stroke="#111" stroke-width="2"/></svg>
          info@velvetorchid.com
        </li>
        <li>
          <svg viewBox="0 0 24 24" aria-hidden="true"><circle cx="12" cy="12" r="10"/><path d="M2 12h20M12 2c3 3 3 17 0 20M12 2c-3 3-3 17 0 20" fill="none" stroke="#fff" stroke-width="1.5"/></svg>
          www.velvetorchid.com
        </li>
      </ul>
    </div>
  </section>
</body>
</html>
```